Veltra - Medical Device Company Needs Box Refined

We are a medical device company needing our packaging refined. This she be clean and sophisticated. The logo must not be change. Please see the attached sample for baseline and sizing.

Industry/Entity Type

It Company

```html
<!DOCTYPE html>
<html lang="en">
<head>
<meta charset="utf-8">
<title>Veltra Hydrophilic Acrylic Intraocular Lens – Box Panels</title>
<link rel="stylesheet" href="https://fonts.googleapis.com/css2?family=Fira+Sans:ital,wght@0,400;0,500;0,700;1,400;1,800&display=swap">
<style>
  :root {
    --page-bg: #e9eef2;
    --panel-white: #ffffff;
    --panel-mist: #f1f5f7;
    --panel-aqua: #aef3f2;
    --side-aqua: #8fe9e6;
    --ink: #111317;
    --icon-ink: #3a3f45;
    --brand-blue: #1f7ad6;
    --brand-gold: #f4e21a;
    --eye-deep: #1f8fe0;
    --eye-light: #6fe0ef;
  }
  * { box-sizing: border-box; margin: 0; padding: 0; }
  html, body {
    width: 1200px;
    height: 900px;
    overflow: hidden;
    background: var(--page-bg);
    font-family: "Fira Sans", Arial, sans-serif;
  }
  .canvas { position: relative; width: 1200px; height: 900px; }

  /* Front face */
  .box-front {
    position: absolute;
    left: 60px;
    top: 130px;
    width: 860px;
    height: 640px;
    background:
      radial-gradient(ellipse 70% 60% at 18% 40%, var(--panel-white) 0%, rgba(255,255,255,0) 70%),
      linear-gradient(120deg, var(--panel-mist) 0%, var(--panel-white) 40%, var(--panel-aqua) 100%);
    box-shadow: 0 10px 30px rgba(30, 60, 90, 0.15);
    overflow: hidden;
  }
  .brand {
    position: absolute;
    left: 34px;
    top: 100px;
    display: flex;
    align-items: center;
    gap: 12px;
  }
  .brand-dot {
    width: 24px; height: 24px;
    border-radius: 50%;
    background: var(--brand-gold);
  }
  .brand-name {
    font-weight: 500;
    font-size: 48px;
    color: var(--brand-blue);
  }
  .product-title {
    position: absolute;
    left: 262px;
    top: 84px;
    font-weight: 800;
    font-style: italic;
    font-size: 52px;
    line-height: 1.1;
    color: var(--ink);
  }
  .product-title .line-two { display: block; padding-left: 30px; }
  .product-title .line-one { display: block; }
  .eye-artwork {
    position: absolute;
    left: 10px;
    top: 280px;
    width: 520px;
    height: 260px;
    border-radius: 60% 40% 55% 45% / 50% 50% 50% 50%;
    background: radial-gradient(ellipse at 40% 45%, var(--eye-deep) 0%, var(--eye-light) 45%, rgba(111,224,239,0) 75%);
    opacity: 0.8;
  }
  .contents {
    position: absolute;
    left: 440px;
    top: 520px;
    color: var(--ink);
    font-style: italic;
    line-height: 1.2;
    font-size: 28px;
  }
  .contents-label { font-weight: 400; }
  .contents-value { font-weight: 800; }

  /* Side panel */
  .box-side {
    position: absolute;
    left: 920px;
    top: 130px;
    width: 170px;
    height: 640px;
    background: linear-gradient(90deg, var(--side-aqua) 0%, var(--panel-white) 45%, var(--panel-mist) 100%);
    box-shadow: 0 10px 30px rgba(30, 60, 90, 0.15);
  }
  .symbol-column {
    position: absolute;
    left: 26px;
    top: 50px;
    display: flex;
    flex-direction: column;
    gap: 42px;
  }
  .symbol { width: 34px; height: 34px; display: block; }
  .side-title {
    position: absolute;
    left: 92px;
    top: 40px;
    writing-mode: vertical-rl;
    font-weight: 700;
    font-size: 22px;
    color: var(--ink);
    white-space: nowrap;
  }
  .side-brand {
    position: absolute;
    left: 56px;
    bottom: 30px;
    writing-mode: vertical-rl;
    display: flex;
    align-items: center;
    gap: 8px;
  }
  .side-brand .brand-dot { width: 16px; height: 16px; }
  .side-brand .brand-name { font-size: 32px; }
</style>
</head>
<body>
  <main class="canvas">
    <section class="box-front">
      <div class="brand">
        <span class="brand-dot"></span>
        <span class="brand-name">Veltra</span>
      </div>
      <h1 class="product-title">
        <span class="line-one">Hydrophilic Acrylic</span>
        <span class="line-two">Intraocular Lens</span>
      </h1>
      <div class="eye-artwork" role="img" aria-label="Stylised blue eye illustration"></div>
      <div class="contents">
        <p class="contents-label">Contents:</p>
        <p class="contents-value">One Intraocular Lens</p>
      </div>
    </section>

    <aside class="box-side">
      <div class="symbol-column">
        <svg class="symbol" viewBox="0 0 34 34" role="img" aria-label="Do not reuse symbol">
          <circle cx="17" cy="17" r="14" fill="none" stroke="var(--icon-ink)" stroke-width="2"/>
          <line x1="7" y1="27" x2="27" y2="7" stroke="var(--icon-ink)" stroke-width="2"/>
        </svg>
        <svg class="symbol" viewBox="0 0 34 34" role="img" aria-label="Do not resterilise symbol">
          <circle cx="17" cy="17" r="14" fill="none" stroke="var(--icon-ink)" stroke-width="2"/>
          <line x1="7" y1="27" x2="27" y2="7" stroke="var(--icon-ink)" stroke-width="2"/>
        </svg>
        <svg class="symbol" viewBox="0 0 34 34" role="img" aria-label="Do not use if package damaged symbol">
          <circle cx="17" cy="17" r="14" fill="none" stroke="var(--icon-ink)" stroke-width="2"/>
          <rect x="11" y="11" width="12" height="12" fill="none" stroke="var(--icon-ink)" stroke-width="2"/>
        </svg>
        <svg class="symbol" viewBox="0 0 34 34" role="img" aria-label="Caution symbol">
          <path d="M17 4 L31 29 H3 Z" fill="none" stroke="var(--icon-ink)" stroke-width="2"/>
          <line x1="17" y1="13" x2="17" y2="21" stroke="var(--icon-ink)" stroke-width="2"/>
        </svg>
        <svg class="symbol" viewBox="0 0 34 34" role="img" aria-label="Sterile symbol">
          <rect x="9" y="3" width="16" height="28" fill="none" stroke="var(--icon-ink)" stroke-width="2"/>
          <line x1="17" y1="3" x2="17" y2="31" stroke="var(--icon-ink)" stroke-width="2"/>
        </svg>
      </div>
      <p class="side-title">Hydrophilic Acrylic Intraocular Lens</p>
      <div class="side-brand">
        <span class="brand-dot"></span>
        <span class="brand-name">Veltra</span>
      </div>
    </aside>
  </main>
</body>
</html>
```